Tidewell Homecare

I am looking to have a website designed for a housekeeping company that looks similar to this one. https://marlowsnestcare.example/

I need 5 websites designed but will start with this one to see how I like it.

Industry/Entity Type

House Cleaning

Coding

Coded - Design and coding required

Number of Pages Required

5+ page

Font styles to use
Serif
Script

Colors
ffffff
fdf9cf
fbf289
fbee3f
d6edf3
86cae7
33a6d7
edf1f8
cedeed

```html
<!DOCTYPE html>
<html lang="en">
<head>
<meta charset="utf-8">
<title>Tidewell Homecare</title>
<link rel="stylesheet" href="https://fonts.googleapis.com/css2?family=Noticia+Text:ital,wght@0,400;0,700;1,400&family=Signika:wght@400;600;700&display=swap">
<style>
:root{
  --teal:#1db3ae;
  --teal-deep:#00aaa6;
  --ink:#2a2a2a;
  --muted:#8a8a8a;
  --line:#b9c3c3;
  --white:#ffffff;
  --cream:#fcf9f2;
  --dark:#2b2a28;
}
*{box-sizing:border-box;margin:0;padding:0}
html,body{width:1200px;height:2776px;overflow:hidden;background:var(--white)}
body{position:relative;font-family:'Signika',sans-serif;color:var(--ink)}
.abs{position:absolute}

/* header */
.site-header{position:absolute;left:0;top:0;width:1200px;height:44px;background:var(--white);border-bottom:1px solid #e4e4e4;z-index:3}
.brand{position:absolute;left:43px;top:2px;width:120px;height:116px;border-radius:50%;background:var(--white);box-shadow:0 2px 6px rgba(0,0,0,.12);display:flex;align-items:center;justify-content:center;text-align:center;z-index:4}
.brand span{font-family:'Signika',sans-serif;font-weight:600;font-size:15px;line-height:1.15;color:var(--teal)}
.main-nav{position:absolute;left:559px;top:13px;display:flex;gap:17px;font-size:10.5px;font-weight:600;letter-spacing:1.6px;text-transform:uppercase;color:#333}
.main-nav .active{color:var(--teal)}
.phone{position:absolute;left:910px;top:11px;display:flex;align-items:center;gap:6px;font-size:13px;color:var(--teal)}
.estimate-btn{position:absolute;left:1028px;top:7px;width:90px;height:26px;border:1px solid var(--teal);border-radius:2px;font-size:10px;font-weight:600;color:var(--teal);display:flex;align-items:center;justify-content:center}

/* hero: photo area runs down to the about section */
.hero{left:0;top:44px;width:1200px;height:1085px;background:
  linear-gradient(180deg,rgba(255,255,255,0) 0%,rgba(255,255,255,0) 48%,rgba(214,200,170,.35) 62%,rgba(200,196,188,.5) 100%),
  linear-gradient(90deg,#d9d6cf 0%,#eeece7 25%,#f1efea 55%,#c9d3d3 80%,#b9c4c2 100%)}
.hero-card{left:323px;top:140px;width:554px;height:334px;border:2px solid var(--teal);border-radius:12px;background:rgba(248,249,248,.88);text-align:center}
.hero-card h1{margin-top:52px;font-family:'Noticia Text',serif;font-weight:400;font-size:28px;line-height:33px;color:#333}
.hero-card p{margin:44px auto 0;width:446px;font-size:11.5px;line-height:21px;text-transform:uppercase;color:#333}
.hero-card svg{margin-top:20px}

/* about */
.about-photo{left:0;top:1129px;width:592px;height:368px;background:linear-gradient(135deg,#e8e6e1,#b7c8d6 45%,#4f7ea8 70%,#c9bca8)}
.about-panel{left:592px;top:1129px;width:604px;height:368px;background:var(--teal-deep)}
.about-panel p{position:absolute;left:39px;top:124px;width:530px;font-size:12.5px;font-weight:600;line-height:21px;color:var(--white)}
.about-btn{position:absolute;left:39px;top:259px;width:212px;height:28px;background:var(--white);color:var(--teal);font-size:19px;display:flex;align-items:center;justify-content:center}

/* contact */
.section-title{font-family:'Noticia Text',serif;font-weight:400;font-size:26px;color:var(--teal);text-align:center;width:1200px;left:0}
.form-field{height:32px;border:1px solid var(--line);background:var(--white);font-family:'Noticia Text',serif;font-size:12.5px;color:var(--muted);padding:0 9px;display:flex;align-items:center;justify-content:space-between}
.submit{left:155px;top:1779px;width:890px;height:31px;background:var(--teal);color:var(--white);font-size:11px;font-weight:700;display:flex;align-items:center;justify-content:center}

/* vendors */
.vendors{left:0;top:1906px;width:1200px;height:372px;background:var(--cream)}
.vendor{width:285px;height:160px;display:flex;align-items:center;justify-content:center;font-family:'Signika',sans-serif;font-weight:600;font-size:21px;color:var(--white)}

/* testimonial */
.testimonial{left:0;top:2278px;width:1200px;height:474px;background:linear-gradient(110deg,#2d2c29 0%,#3a3935 50%,#2f6f91 72%,#b4563f 90%,#d98d43 100%)}
.quote{left:233px;top:2394px;width:440px;font-style:italic;font-size:24px;line-height:36px;color:var(--white)}
.author{left:232px;top:2488px;font-size:23px;color:var(--white)}

/* footer */
.site-footer{left:0;top:2752px;width:1200px;height:24px;background:var(--teal);color:var(--white);font-size:12px;font-weight:600;display:flex;align-items:center;justify-content:center}
.to-top{left:1165px;top:2735px;width:28px;height:25px;background:#111;border-radius:2px;display:flex;align-items:center;justify-content:center}
</style>
</head>
<body>

<header class="site-header">
  <nav class="main-nav">
    <span class="active">Home</span><span>Services</span><span>Gift Cards</span><span>About</span><span>Contact</span>
  </nav>
  <div class="phone">
    <svg width="13" height="13" viewBox="0 0 24 24"><path fill="#1db3ae" d="M6.6 10.8a15.1 15.1 0 0 0 6.6 6.6l2.2-2.2a1 1 0 0 1 1-.25 11.4 11.4 0 0 0 3.6.57 1 1 0 0 1 1 1V20a1 1 0 0 1-1 1A17 17 0 0 1 3 4a1 1 0 0 1 1-1h3.5a1 1 0 0 1 1 1c0 1.25.2 2.45.57 3.57a1 1 0 0 1-.25 1z"/></svg>
    202-555-0148
  </div>
  <div class="estimate-btn">FREE ESTIMATE</div>
</header>
<div class="brand"><span>Tidewell<br>Homecare</span></div>

<section class="abs hero" role="img" aria-label="Bright living room with white walls, sofa, armchair and floor lamp"></section>
<div class="abs hero-card">
  <h1>THE IMPORTANCE OF GOOD<br>HOUSEKEEPING</h1>
  <p>We all know how important having a good housekeeper is. Trust the team with 25 years of professional experience for your Cedar Valley home or office space.</p>
  <svg width="30" height="18" viewBox="0 0 30 18"><path d="M3 3l12 11L27 3" fill="none" stroke="#0e6f6c" stroke-width="5"/></svg>
</div>

<section class="abs about-photo" role="img" aria-label="Cleaning crew in aprons and overalls with mops, buckets and a vacuum"></section>
<section class="abs about-panel">
  <p>Our team is what sets us apart, and we have the best staff around. Our friendly, caring crew loves the Cedar Valley and its diverse community and this is evident in their work. Tidewell Homecare is twenty plus years in the making and going stronger than ever. We look forward to many more years of serving this valley as well as enjoying all it has to offer.</p>
  <div class="about-btn">GET TO KNOW US</div>
</section>

<h2 class="abs section-title" style="top:1586px">Free Estimate / Contact Us</h2>
<div class="abs form-field" style="left:155px;top:1666px;width:216px">Name *</div>
<div class="abs form-field" style="left:380px;top:1666px;width:215px">Email *</div>
<div class="abs form-field" style="left:605px;top:1666px;width:215px">City *</div>
<div class="abs form-field" style="left:830px;top:1666px;width:215px">Square Footage *</div>
<div class="abs form-field" style="left:155px;top:1722px;width:216px">Property type *<svg width="8" height="5"><path d="M0 0h8L4 5z" fill="#333"/></svg></div>
<div class="abs form-field" style="left:380px;top:1722px;width:215px">Type of Cleaning *<svg width="8" height="5"><path d="M0 0h8L4 5z" fill="#333"/></svg></div>
<div class="abs form-field" style="left:605px;top:1722px;width:215px">Frequency *<svg width="8" height="5"><path d="M0 0h8L4 5z" fill="#333"/></svg></div>
<div class="abs form-field" style="left:830px;top:1722px;width:215px">Date *</div>
<div class="abs submit">SUBMIT</div>

<section class="abs vendors"></section>
<h2 class="abs section-title" style="top:1978px">Prefered Vendors</h2>
<div class="abs vendor" style="left:156px;top:2032px;background:#4a4f3e" role="img" aria-label="Mountain lodge among aspen trees">Ridge Rentals by Owner</div>
<div class="abs vendor" style="left:458px;top:2032px;background:#5e5a56">Brightline Cleaning</div>
<div class="abs vendor" style="left:759px;top:2032px;background:#3b3b3d">The Linen Loft</div>

<section class="abs testimonial" role="img" aria-label="Cleaning supplies: gloves, brushes and soap bottles on a dark wooden table"></section>
<p class="abs quote">Tidewell Homecare is the best. Great crews. Thorough and trustworthy.</p>
<p class="abs author">- Dana Reyes</p>
<svg class="abs" style="left:166px;top:2503px" width="10" height="14" viewBox="0 0 10 14"><path d="M8 1L2 7l6 6" fill="none" stroke="#fff" stroke-width="2"/></svg>
<svg class="abs" style="left:761px;top:2503px" width="10" height="14" viewBox="0 0 10 14"><path d="M2 1l6 6-6 6" fill="none" stroke="#fff" stroke-width="2"/></svg>
<svg class="abs" style="left:466px;top:2659px" width="5" height="5"><circle cx="2.5" cy="2.5" r="2.5" fill="#111"/></svg>

<footer class="abs site-footer">Tidewell Homecare</footer>
<div class="abs to-top"><svg width="12" height="13" viewBox="0 0 12 13"><path d="M6 12V2M1.5 6L6 1.5 10.5 6" fill="none" stroke="#fff" stroke-width="2"/></svg></div>

</body>
</html>
```